■概要 ・TWRへの出稿用バナー作成をしていただける方を募集します。 ---------------- ■注意点 ご提案頂きましたバナー案について、SNSへの投稿・Webサイトへのアップ等を行わないようにお願いします。 採用前、採用後に大なり小なり修正が発生する可能性があります。 ※承諾頂ける方のみコンペへの参加をお願いします。 ---------------- ■依頼詳細 ・バナー内にテキストを挿入する場合は、テキストレイヤーで挿入してください。 ・テキストはおよそ1/4サイズで表示される事を考慮して制作して下さい。 ・配信時は制作したバナーがスマホの画面幅程度に縮小されて表示されます。テキストの可読性を考慮して制作お願いします ・バナー広告を見て、押したくなるようなバナー作成をお願いします。 ■配信先 http://korisaku.com/ ※対応方法の一部変更(9/27内容修正) ・コンペは今まで通り、1200×628 で行います。 ・採用になった作品の納品時に300×300のバナーを作成して頂き一緒に納品して頂きたいです ※300×300のバナーは採用バナーの簡易版としてつけて頂けると幸いです。 ⇒そのまま縮小というより、「メイン画像+社名(ロゴ)+一言キャッチ」くらい簡易的でOKです。 小さいバナーですので可読性を考慮して頂けると幸いです。 ■サイズと枚数 【コンペ】 ・1200 x 628 ・1枚 【納品時】 ・1200 x 628 → 1枚 ・300×300→ 1枚 ■納品ファイル ・フォトショップ形式(.psd) ■連絡事項 土日・祝日は対応することができません。 平日は9~18時までにご連絡いただければ、当日。 それ以降は翌日にご返信いたします。 ※TWRガイドラインに沿った内容である事 TWR掲載ガイドライン関連資料(https://help.velnora.com/adpolicyhub/topic/4830217?hl=ja&ref_topic=5172084,6093471,) ※他で登録されているデザインや商標の転用など、他社の知的財産権を侵すこと ※他のクライアントへ既に提案した内容の転用など たくさんのウェブデザイナーの方からのご提案をお待ちしております。 |
クライアント様が気に入りましたので、採用致します。
これからも沢山募集しますので、よろしくお願い致します。

```html
<!DOCTYPE html>
<html lang="ja">
<head>
<meta charset="utf-8">
<title>アトリエ キヌ — online store</title>
<link href="https://fonts.googleapis.com/css2?family=Noto+Serif+JP:wght@400;500&display=swap" rel="stylesheet">
<style>
  :root {
    --marble-light: #faf8f5;
    --marble-mid: #f1ebe4;
    --marble-vein: rgba(214, 202, 190, 0.45);
    --ink-brown: #4a3428;
    --button-brown: #4f3529;
    --button-text: #ffffff;
    --photo-dress-light: #fbfaf7;
    --photo-dress-shade: #dcd8d2;
    --photo-bouquet-purple: #8c7cae;
    --photo-bouquet-green: #9aa57c;
    --photo-shoes-yellow: #f2cf3a;
    --photo-bouquet-a: #e3e9f0;
    --photo-bouquet-b: #a9bcd0;
    --photo-frame-a: #c79a5e;
    --photo-frame-b: #c98fb6;
  }
  html, body {
    margin: 0;
    padding: 0;
    width: 1200px;
    height: 628px;
    overflow: hidden;
  }
  .banner {
    position: relative;
    width: 1200px;
    height: 628px;
    overflow: hidden;
    font-family: "Noto Serif JP", serif;
    color: var(--ink-brown);
    background:
      linear-gradient(155deg, transparent 38%, var(--marble-vein) 40%, transparent 42%),
      linear-gradient(25deg, transparent 58%, var(--marble-vein) 60%, transparent 62%),
      radial-gradient(ellipse at 55% 40%, var(--marble-light), var(--marble-mid));
  }
  .photo {
    position: absolute;
  }
  .photo--bride {
    left: 0;
    top: 150px;
    width: 300px;
    height: 478px;
    background:
      radial-gradient(ellipse 70px 60px at 140px 110px, var(--photo-bouquet-purple), rgba(140,124,174,0) 100%),
      radial-gradient(ellipse 40px 30px at 90px 90px, var(--photo-bouquet-green), rgba(154,165,124,0) 100%),
      radial-gradient(ellipse 70px 60px at 180px 420px, var(--photo-shoes-yellow), rgba(242,207,58,0) 100%),
      radial-gradient(ellipse 40px 60px at 120px 460px, var(--photo-shoes-yellow), rgba(242,207,58,0) 100%),
      linear-gradient(90deg, var(--photo-dress-shade) 0%, var(--photo-dress-light) 55%, rgba(251,250,247,0) 100%);
    -webkit-mask-image: linear-gradient(180deg, rgba(0,0,0,0) 0%, #000 18%);
    mask-image: linear-gradient(180deg, rgba(0,0,0,0) 0%, #000 18%);
  }
  .photo--bouquet {
    left: 830px;
    top: 0;
    width: 270px;
    height: 250px;
    border-radius: 50%;
    background: radial-gradient(circle, var(--photo-bouquet-a) 30%, var(--photo-bouquet-b) 70%, rgba(169,188,208,0) 72%);
  }
  .photo--frame {
    left: 860px;
    top: 360px;
    width: 290px;
    height: 270px;
    transform: rotate(-6deg);
    border: 14px solid var(--photo-frame-a);
    background: radial-gradient(circle at 50% 50%, var(--photo-frame-b), #b47aa4);
  }
  .content {
    position: absolute;
    left: 300px;
    width: 600px;
    top: 0;
    text-align: center;
  }
  .tagline {
    position: absolute;
    top: 134px;
    width: 100%;
    margin: 0;
    font-size: 25px;
    font-weight: 500;
    letter-spacing: 1px;
  }
  .brand-name {
    position: absolute;
    top: 212px;
    width: 100%;
    margin: 0;
    font-size: 62px;
    font-weight: 400;
    letter-spacing: 4px;
  }
  .brand-kana {
    position: absolute;
    top: 360px;
    width: 100%;
    margin: 0;
    font-size: 30px;
    font-weight: 500;
    letter-spacing: 4px;
  }
  .store-button {
    position: absolute;
    left: 100px;
    top: 442px;
    width: 400px;
    height: 60px;
    border-radius: 30px;
    background: var(--button-brown);
    color: var(--button-text);
    text-decoration: none;
    display: flex;
    align-items: center;
    justify-content: center;
    font-size: 27px;
    letter-spacing: 1px;
  }
  .store-button svg {
    position: absolute;
    left: 22px;
    top: 12px;
  }
</style>
</head>
<body>
<main class="banner">
  <div class="photo photo--bride" role="img" aria-label="白いウエディングドレスの花嫁が紫のブーケを持ち、黄色いスニーカーを履いた写真"></div>
  <div class="photo photo--bouquet" role="img" aria-label="白いアネモネと青い花のプリザーブドフラワーブーケの写真"></div>
  <div class="photo photo--frame" role="img" aria-label="木製フレームに入ったピンクと紫のバラのプリザーブドフラワーの写真"></div>

  <section class="content">
    <p class="tagline">プリザーブドフラワー通販専門店</p>
    <h1 class="brand-name">atelier kinu</h1>
    <p class="brand-kana">アトリエ キヌ</p>
    <a class="store-button" href="#">
      <svg width="46" height="36" viewBox="0 0 46 36" aria-hidden="true">
        <path d="M3 4 H10 L14 24 H38 L42 9 H12" fill="none" stroke="#fff" stroke-width="2.5" stroke-linejoin="round"/>
        <path d="M18 9 V24 M24 9 V24 M30 9 V24 M36 9 V24 M13 16 H40" stroke="#fff" stroke-width="1.5"/>
        <circle cx="17" cy="30" r="3" fill="#fff"/>
        <circle cx="35" cy="30" r="3" fill="#fff"/>
      </svg>
      online store
    </a>
  </section>
</main>
</body>
</html>
```